Law Office Business Card

We need a business card design to include the following information:
Name of Firm: Brennick Law Group, P.A.
Address: 4627 Sandlot Ave, Ste 208, Harbor Point, FL 33990
Phone: 561-555-0148
Fax: 561-555-0193
Website: http://www.tbrennicklaw.example

We Need a place for the Person's name and email address. Please start with the following:
Lorna K. Dwyer, Esq.
lorna@tbrennicklaw.example

```html
<!DOCTYPE html>
<html lang="en">
<head>
<meta charset="utf-8">
<title>Brennick Law Group – Business Card</title>
<link href="https://fonts.googleapis.com/css2?family=Jost:wght@400;500;600&display=swap" rel="stylesheet">
<style>
  :root {
    --backdrop: #2a2a2c;
    --card: #050505;
    --gold: #b9a88e;
    --gold-soft: #8f8270;
    --line: #a8977c;
  }
  * { box-sizing: border-box; margin: 0; padding: 0; }
  html, body {
    width: 1200px; height: 904px; overflow: hidden;
    background: var(--backdrop);
    font-family: "Jost", sans-serif;
  }
  .canvas { position: relative; width: 1200px; height: 904px; }
  .card {
    position: absolute; left: 270px;
    width: 660px; height: 377px;
    background: var(--card);
    border-radius: 22px;
    box-shadow: 0 10px 30px rgba(0,0,0,.45);
    overflow: hidden;
  }
  .card--front { top: 50px; }
  .card--back { top: 477px; }

  /* front */
  .front-mark {
    position: absolute; inset: 0;
    display: flex; align-items: center; justify-content: center; gap: 12px;
  }
  .mark-square { width: 16px; height: 16px; border: 1.5px solid var(--gold); }
  .firm-wordmark {
    color: var(--gold); font-weight: 500; font-size: 20px;
    letter-spacing: 4px; text-transform: uppercase;
  }

  /* back */
  .corner { position: absolute; left: 0; top: 0; }
  .back-logo {
    position: absolute; left: 44px; top: 150px; width: 180px;
    display: flex; flex-direction: column; align-items: flex-start; gap: 10px;
  }
  .back-logo .mark-square { width: 22px; height: 22px; }
  .back-logo .firm-wordmark { font-size: 21px; letter-spacing: 3px; line-height: 1.15; }

  .person-name {
    position: absolute; left: 252px; top: 222px;
    color: var(--gold); font-weight: 600; font-size: 15px; letter-spacing: .3px;
    white-space: nowrap;
  }
  .address {
    position: absolute; left: 252px; top: 258px;
    color: var(--gold-soft); font-size: 13px; line-height: 18px; font-weight: 400;
    white-space: nowrap;
  }
  .contacts {
    position: absolute; left: 468px; top: 198px;
    list-style: none; color: var(--gold-soft); font-size: 11.5px;
    white-space: nowrap;
  }
  .contacts li { display: flex; align-items: center; gap: 7px; height: 17px; }
  .contacts svg { width: 11px; height: 11px; flex: none; }
</style>
</head>
<body>
<main class="canvas">

  <section class="card card--front" aria-label="Card front">
    <div class="front-mark">
      <span class="mark-square"></span>
      <span class="firm-wordmark">Brennick Law Group</span>
    </div>
  </section>

  <section class="card card--back" aria-label="Card back">
    <svg class="corner" width="660" height="377" viewBox="0 0 660 377" aria-hidden="true">
      <g stroke="var(--line)" stroke-width="1.3" fill="none">
        <polyline points="478,28 604,28 604,132"/>
        <polyline points="58,292 58,344 238,344"/>
        <line x1="380" y1="192" x2="628" y2="192"/>
        <line x1="252" y1="244" x2="448" y2="244"/>
        <line x1="458" y1="200" x2="458" y2="272"/>
      </g>
    </svg>

    <div class="back-logo">
      <span class="mark-square"></span>
      <span class="firm-wordmark">Brennick Law<br>Group</span>
    </div>

    <p class="person-name">Lorna K. Dwyer, Esq.</p>
    <p class="address">
      Brennick Law Group, P.A.<br>
      4627 Sandlot Ave, Ste 208<br>
      Harbor Point, FL 33990
    </p>

    <ul class="contacts">
      <li>
        <svg viewBox="0 0 12 12"><path d="M3 1.5l1.6 2.2-1 1a6 6 0 0 0 3.7 3.7l1-1 2.2 1.6-.9 1.5C5.4 10.3 1.7 6.6 1.5 2.4z" fill="var(--gold-soft)"/></svg>
        561-555-0148
      </li>
      <li>
        <svg viewBox="0 0 12 12"><rect x="3" y="1.5" width="6" height="3" fill="none" stroke="var(--gold-soft)"/><rect x="1" y="4.5" width="10" height="5" rx="1" fill="var(--gold-soft)"/></svg>
        561-555-0193
      </li>
      <li>
        <svg viewBox="0 0 12 12"><rect x="1" y="2.5" width="10" height="7" rx="1" fill="var(--gold-soft)"/><path d="M1.5 3l4.5 3.5L10.5 3" stroke="#050505" fill="none"/></svg>
        lorna@tbrennicklaw.example
      </li>
      <li>
        <svg viewBox="0 0 12 12"><g fill="none" stroke="var(--gold-soft)"><circle cx="6" cy="6" r="4.8"/><ellipse cx="6" cy="6" rx="2" ry="4.8"/><line x1="1.2" y1="6" x2="10.8" y2="6"/></g></svg>
        www.tbrennicklaw.example
      </li>
    </ul>
  </section>

</main>
</body>
</html>
```